Commercial painting company is looking for a creative website designer.

Hi, we just completed our logo project and now ready to launch our website. The project will be done on Squarespace platform. It will contain:
Page 1 HOME
Page 2 SERVICES
Page 3 PICTURES
The content will be written by us. I am not sure bout the pictures, I do not have any to provide. I can buy stock photos if needed.
We are commercial only painting company and have to appeal to commercial, industrial property mangers. We will need CALL, REQUEST FOR ESTIMATE buttons.
If possible to have a live picture on home page would be great. Thank you
Target Market(s)
Property Managers
Industry/Entity Type
Commercial Painting
Other font styles liked:
- Poppins

```html
<!DOCTYPE html>
<html lang="en">
<head>
<meta charset="utf-8">
<title>Brightcoat Commercial — Commercial &amp; Industrial Painting</title>
<link href="https://fonts.googleapis.com/css2?family=Poppins:wght@300;400;500;600&display=swap" rel="stylesheet">
<style>
  :root{
    --navy:#0b3a6b;
    --navy-deep:#0a2f63;
    --strip:#0f5b96;
    --accent:#3b86d1;
    --band-a:#123a7a;
    --band-b:#30609f;
    --tile:#1d3f74;
    --pale:#eef1f8;
    --red:#cc1a10;
    --ink:#111;
    --body:#555;
    --white:#fff;
  }
  *{box-sizing:border-box;margin:0;padding:0}
  html,body{width:1200px;height:3942px;overflow:hidden}
  body{position:relative;font-family:"Poppins",sans-serif;color:var(--ink);background:var(--white)}
  .abs{position:absolute}
  .media{position:absolute;display:block}

  /* header */
  .site-header{left:0;top:0;width:1200px;height:67px;background:var(--white)}
  .brand{left:168px;top:20px;display:flex;align-items:center;gap:10px;font-size:17px;font-weight:600;color:var(--navy)}
  .brand-dot{width:26px;height:26px;border-radius:50%;background:var(--navy)}
  .nav{left:510px;top:30px;display:flex;gap:30px;font-size:11px;font-weight:500}
  .query{left:918px;top:18px;font-size:9px;color:#777;line-height:1.5}
  .query strong{display:flex;align-items:center;gap:6px;font-size:11px;color:var(--ink);font-weight:600}

  /* hero */
  .hero-band{left:0;top:67px;width:1200px;height:225px;background:var(--navy)}
  .hero-strip{left:0;top:67px;width:104px;height:520px;background:linear-gradient(var(--navy),var(--strip))}
  .hero-title{left:176px;top:160px;font-size:34px;font-weight:400;line-height:44px;color:var(--white)}
  .btn-light{left:824px;top:176px;width:191px;height:38px;background:var(--accent);color:var(--white);font-size:11px;display:flex;align-items:center;justify-content:center;gap:14px}
  .hero-photo{left:104px;top:292px;width:1096px;height:423px;background:linear-gradient(90deg,#a9c46a 0%,#e6e8e3 25%,#f0eee9 60%,#2c4fb0 88%,#22409a 100%)}
  .dots{left:63px;top:402px;display:flex;flex-direction:column;gap:12px}
  .dots span{width:9px;height:9px;border-radius:50%;background:#5fa0dc}
  .dots span.ring{background:none;border:1.5px solid #5fa0dc}

  /* about */
  .about-title{left:245px;top:786px;font-size:34px;font-weight:600;line-height:42px;letter-spacing:-0.5px}
  .about-copy{left:246px;top:900px;width:335px;font-size:13px;line-height:23.8px;color:var(--body)}
  .btn-dark{left:246px;top:1127px;width:193px;height:40px;background:var(--navy-deep);color:var(--white);font-size:11px;display:flex;align-items:center;justify-content:center;gap:14px}
  .about-photo-a{left:615px;top:920px;width:236px;height:270px;background:linear-gradient(160deg,#c9b79a,#8d7d66 60%,#2f8a4a)}
  .about-photo-b{left:866px;top:876px;width:291px;height:335px;background:linear-gradient(180deg,#f1e4a6,#e8d68c 60%,#5d6fa8)}

  /* services band */
  .services-band{left:0;top:1254px;width:1200px;height:481px;background:linear-gradient(90deg,var(--band-a),var(--band-b))}
  .services-lead{left:300px;top:1345px;width:600px;text-align:center;color:#e6edf8;font-size:19px;font-weight:300;line-height:28px}
  .tiles{left:276px;top:1508px;display:flex;gap:12px}
  .tile{width:122px;height:86px;background:var(--tile);color:var(--white);font-size:11px;display:flex;flex-direction:column;align-items:center;justify-content:center;gap:10px}
  .arrow-nav{top:1540px;color:var(--white);font-size:22px}

  .pale{left:0;top:1735px;width:1200px;height:831px;background:var(--pale)}
  .commercial-photo{left:245px;top:1673px;width:710px;height:400px;background:linear-gradient(90deg,#f2f3f2,#e5e7e6 50%,#a5a9a8 80%,#d7d9d8)}
  .card{background:#f5f5f6;padding:0 32px}
  .card h3{font-size:19px;font-weight:500;margin-bottom:10px}
  .card p{font-size:13px;line-height:20.5px;color:var(--body)}
  .card .more{margin-top:18px;font-size:11px;font-weight:600;color:var(--navy-deep);display:flex;gap:8px}
  .card-commercial{left:295px;top:1710px;width:296px;height:335px;padding-top:68px}
  .industrial-photo{left:245px;top:2119px;width:367px;height:364px;background:linear-gradient(160deg,#2f6fb9,#4f8bd0 50%,#8ab13a 70%,#2a2e33)}
  .card-industrial{left:626px;top:2119px;width:329px;height:364px;background:var(--white);padding:88px 42px 0}

  /* palette */
  .palette-photo{left:0;top:2566px;width:833px;height:367px;background:linear-gradient(100deg,#1f6a5f 0%,#2f5aa8 20%,#e24a3a 45%,#f2822c 65%,#f6c33c 85%,#f3e08a 100%)}
  .palette-red{left:833px;top:2566px;width:367px;height:367px;background:var(--red)}
  .palette-text{left:873px;top:2683px;width:300px;font-size:25px;font-weight:300;line-height:34px;color:var(--white)}
  .palette-link{left:877px;top:2793px;font-size:11px;color:var(--white);display:flex;gap:22px}

  /* testimonials */
  .testi-bg{left:0;top:2933px;width:1200px;height:1009px;background:linear-gradient(180deg,#f8f8f8,#efefee)}
  .crew-photo{left:150px;top:3360px;width:470px;height:180px;background:linear-gradient(90deg,rgba(120,110,100,.35),rgba(230,230,230,.2) 60%,rgba(80,100,170,.3))}
  .quote-mark{left:196px;top:3078px;font-size:64px;font-weight:600;line-height:1;color:var(--ink)}
  .testi-title{left:251px;top:3085px;font-size:32px;font-weight:300;line-height:40px}
  .testi-copy{left:254px;top:3186px;width:400px;font-size:12px;line-height:20px;color:var(--body)}
  .testi-name{left:254px;top:3360px;font-size:11px;color:var(--red)}
  .testi-photo-b{left:828px;top:3175px;width:239px;height:187px;background:linear-gradient(90deg,#3c4a3c,#3f8a52 55%,#7e8280)}
  .testi-photo-a{left:744px;top:3218px;width:121px;height:120px;background:linear-gradient(135deg,#e8b23a,#c98f2a);border:2px solid var(--white)}

  /* contact */
  .contact-card{left:127px;top:3541px;width:929px;height:314px;background:var(--white);border-radius:18px}
  .contact-email{left:266px;top:3600px;font-size:19px;color:#1d4fa8}
  .contact-title{left:266px;top:3644px;font-size:29px;font-weight:500;line-height:38px}
  .divider{left:652px;top:3598px;width:1px;height:222px;background:#999}
  .contact-label{left:721px;top:3604px;font-size:10px;font-weight:600;color:var(--red)}
  .address{left:721px;top:3630px;font-size:16px;line-height:23px}
  .meta{left:721px;display:flex;align-items:center;gap:8px;font-size:11px;color:#444}
  .btn-visit{left:723px;top:3751px;width:127px;height:29px;background:#1242a8;color:var(--white);font-size:10px;display:flex;align-items:center;justify-content:center}
  .copyright{left:0;top:3894px;width:1200px;text-align:center;font-size:11px;color:#444}
</style>
</head>
<body>

<header class="abs site-header">
  <div class="abs brand"><span class="brand-dot"></span>Brightcoat Commercial</div>
  <nav class="abs nav"><span>Home</span><span>Service</span><span>Work Gallery</span><span>Contact Us</span></nav>
  <div class="abs query">For any query<strong>
    <svg width="11" height="11" viewBox="0 0 24 24"><path fill="#111" d="M6.6 10.8a15 15 0 0 0 6.6 6.6l2.2-2.2c.3-.3.7-.4 1-.2 1.1.4 2.3.6 3.6.6.6 0 1 .4 1 1V20c0 .6-.4 1-1 1A17 17 0 0 1 3 4c0-.6.4-1 1-1h3.5c.6 0 1 .4 1 1 0 1.3.2 2.5.6 3.6.1.3 0 .7-.2 1z"/></svg>
    (555) 014-2290</strong></div>
</header>

<section>
  <div class="abs hero-band"></div>
  <div class="abs hero-strip"></div>
  <h1 class="abs hero-title">A premier commercial &amp; industrial<br>painting company.</h1>
  <div class="abs btn-light">Schedule a Consultation <span>↗</span></div>
  <div class="media hero-photo" role="img" aria-label="Painter rolling green paint on a wall while a worker kneels on the floor"></div>
  <div class="abs dots"><span></span><span></span><span class="ring"></span><span></span></div>
</section>

<section>
  <h2 class="abs about-title">We are a commercial painting<br>company you can rely on.</h2>
  <p class="abs about-copy">We offer a full spectrum of commercial painting projects and structures, using the highest quality materials, workmanship, and level of service. Brightcoat Crew provides the highest quality of service and guarantees reliability every time. We take pride in the training of our members, with our senior estimator having over 50 years experience in the industry and many other employees having over 35.</p>
  <div class="abs btn-dark">Schedule a Consultation <span>↗</span></div>
  <div class="media about-photo-a" role="img" aria-label="Painter on a green scissor lift beside a tall wall"></div>
  <div class="media about-photo-b" role="img" aria-label="Rope-access painters working on a yellow building facade"></div>
</section>

<section>
  <div class="abs services-band"></div>
  <p class="abs services-lead">Our professional and certified building contractors have years of professional experience painting high-rises, mid-rises, hotels, hospitals, office buildings, shopping centers and industrial buildings throughout USA.</p>
  <span class="abs arrow-nav" style="left:244px">‹</span>
  <div class="abs tiles">
    <div class="tile"><svg width="24" height="24" viewBox="0 0 24 24" fill="none" stroke="#fff" stroke-width="1.3"><rect x="5" y="3" width="10" height="18"/><rect x="15" y="10" width="5" height="11"/><path d="M8 7h4M8 11h4M8 15h4"/></svg>Office buildings</div>
    <div class="tile"><svg width="24" height="24" viewBox="0 0 24 24" fill="none" stroke="#fff" stroke-width="1.3"><path d="M3 8h18v13H3zM4 3h16l1 5H3z"/><rect x="9" y="13" width="6" height="8"/></svg>Retail buildings</div>
    <div class="tile"><svg width="24" height="24" viewBox="0 0 24 24" fill="none" stroke="#fff" stroke-width="1.3"><rect x="4" y="4" width="16" height="17"/><path d="M8 4v17M12 4v17M16 4v17"/></svg>High rise buildings</div>
    <div class="tile"><svg width="24" height="24" viewBox="0 0 24 24" fill="none" stroke="#fff" stroke-width="1.3"><path d="M3 9l9-5 9 5v12H3z"/><rect x="7" y="13" width="10" height="8"/><path d="M7 16h10"/></svg>Warehouses</div>
    <div class="tile"><svg width="24" height="24" viewBox="0 0 24 24" fill="none" stroke="#fff" stroke-width="1.3"><rect x="4" y="6" width="16" height="15"/><path d="M12 2v6M9 5h6M8 12h2M14 12h2M8 16h2M14 16h2"/></svg>Healthcare Facilities</div>
  </div>
  <span class="abs arrow-nav" style="left:946px">›</span>
</section>

<section>
  <div class="abs pale"></div>
  <div class="media commercial-photo" role="img" aria-label="Bright open-plan office with glass walls and pendant lights"></div>
  <article class="abs card card-commercial">
    <h3>Commercial Painting</h3>
    <p>First impressions are often last impressions. This is especially true for your commercial space. Our commercial painting services help you attract and entice customers from all walks of life.</p>
    <div class="more">Get free estimate <span>↗</span></div>
  </article>
  <div class="media industrial-photo" role="img" aria-label="Industrial painters in safety gear on a lift painting a blue steel structure"></div>
  <article class="abs card card-industrial">
    <h3>Industrial Painting</h3>
    <p>Our experience with industrial painting includes everything from bridges to warehouses. Working around our clients’ schedules, we ensure that production is not compromised while we work.</p>
    <div class="more">Get free estimate <span>↗</span></div>
  </article>
</section>

<section>
  <div class="media palette-photo" role="img" aria-label="Fanned paint colour swatch cards in a rainbow of shades"></div>
  <div class="abs palette-red"></div>
  <p class="abs palette-text">Choose a color palette that fits the size of your industries.</p>
  <div class="abs palette-link">Get free estimate <span>↗</span></div>
</section>

<section>
  <div class="abs testi-bg"></div>
  <div class="media crew-photo" role="img" aria-label="Faded image of painters spraying and rolling a ceiling"></div>
  <div class="abs quote-mark">“</div>
  <h2 class="abs testi-title">Here's what our satisfied<br>clients are saying...</h2>
  <p class="abs testi-copy">Lorem ipsum dolor sit. amet, consecteteur adipiscing elit, sed do eiusmod tempor incididunt ut labore et dolore. Lorem ipsum dolor sit amet, consectetur adipiscing elit. Parkett als Landhausdielen bringen mit ihrer ruhigen und edlen oder rustikalen Ausstrahlung eine besondere Atmosphäre in Ihr Zuhause. Der natürliche Charakter entsteht durch großzügige Formate. Eine wahlweise glatte, gebürstete oder gehobelte</p>
  <div class="abs testi-name">Dana Ruell</div>
  <div class="media testi-photo-b" role="img" aria-label="Rope-access painter coating a building wall green"></div>
  <div class="media testi-photo-a" role="img" aria-label="Close-up of peeling yellow paint"></div>

  <div class="abs contact-card"></div>
  <div class="abs contact-email">hello@brightcoat.example</div>
  <h2 class="abs contact-title">We’re ready to meet<br>with you today to<br>discuss your exterior<br>painting needs.</h2>
  <div class="abs divider"></div>
  <div class="abs contact-label">Contact.</div>
  <p class="abs address">214 Kestrel Avenue Harbor<br>Point, CA 90000</p>
  <div class="abs meta" style="top:3688px"><svg width="11" height="11" viewBox="0 0 24 24"><path fill="#333" d="M6.6 10.8a15 15 0 0 0 6.6 6.6l2.2-2.2c.3-.3.7-.4 1-.2 1.1.4 2.3.6 3.6.6.6 0 1 .4 1 1V20c0 .6-.4 1-1 1A17 17 0 0 1 3 4c0-.6.4-1 1-1h3.5c.6 0 1 .4 1 1 0 1.3.2 2.5.6 3.6.1.3 0 .7-.2 1z"/></svg>Call us : 555-014-2290</div>
  <div class="abs meta" style="top:3710px"><svg width="11" height="11" viewBox="0 0 24 24" fill="none" stroke="#333" stroke-width="2.4"><circle cx="12" cy="12" r="9"/><path d="M12 7v5l3 2"/></svg>Mon - Fri - 7:00am - 4:30pm</div>
  <div class="abs btn-visit">Visit to our location</div>
  <p class="abs copyright">Copyright ©2023, Brightcoat Commercial. All rights reserved.</p>
</section>

</body>
</html>
```